Flashy and colorful banner for an orange grower

Hi, I need a graphic for an advertising banner (80x200cm) to be placed next to the sales van. So far we have tried to highlight the naturalness of our products. With this banner we would like to highlight the ancient Sicilian tradition, with the typical decorations, I attach some photos as an example. We will sell our products far from Sicily, so I would like to exalt our origin.
We would like to dare with a colorful and amazing design, to capture the attention of passers-by.
It might be nice to insert or rework the decoration within our logo.
I would like to insert 4 of our offers inside the banner, only in the upper part, from the middle up.
The text is:
DAL CUORE DELLA SICILIA
ARANCIA TAROCCO
ALLA RINFUSA
5€ BORSA
DA SPREMERE
10€ CASSETTA
DA TAVOLA
15€ CASSETTA
SELEZIONE PREMIUM
20€ CASSETTA
Thanks for your time

```html
<!DOCTYPE html>
<html lang="it">
<head>
<meta charset="utf-8">
<title>Agrumeto Solare – Arancia Tarocco</title>
<link href="https://fonts.googleapis.com/css2?family=Staatliches&display=swap" rel="stylesheet">
<style>
  :root{
    --green-light:#2fb257;
    --green-mid:#15803a;
    --green-dark:#0b3d1f;
    --green-text:#1e6a37;
    --green-bright:#20a33a;
    --orange:#e8652d;
    --orange-soft:#f5a031;
    --orange-red:#dc5a24;
    --red:#e02a24;
    --white:#ffffff;
    --paper-end:#e2e2e2;
  }
  *{margin:0;padding:0;box-sizing:border-box}
  html,body{width:1200px;height:2804px;overflow:hidden;background:#dfe4e8}
  .banner{
    position:relative;width:1200px;height:2804px;
    font-family:"Staatliches",Impact,sans-serif;
  }
  .banner__ornament{
    position:absolute;inset:0;
    background:linear-gradient(180deg,var(--green-light) 0%,var(--green-mid) 50%,var(--green-dark) 100%);
  }
  .banner__panel{
    position:absolute;left:130px;right:130px;top:90px;bottom:90px;
    background:linear-gradient(180deg,var(--white) 40%,var(--paper-end) 100%);
    display:flex;flex-direction:column;align-items:center;text-align:center;
  }
  .brand{margin-top:60px;display:flex;flex-direction:column;align-items:center}
  .brand__mark{width:230px;height:230px;border-radius:50%;background:var(--orange-soft)}
  .brand__name{margin-top:30px;font-size:92px;line-height:1;color:var(--green-text);letter-spacing:2px}
  .headline{margin-top:90px;line-height:.95}
  .headline__top{font-size:178px;color:var(--orange)}
  .headline__bottom{font-size:158px;color:var(--green-text)}
  .variety{
    margin-top:14px;width:760px;padding:10px 0 4px;
    background:linear-gradient(90deg,var(--red),var(--orange-soft));
    color:var(--white);font-size:100px;line-height:1;transform:rotate(-1deg);
  }
  .offers{margin-top:70px;display:flex;flex-direction:column;gap:78px}
  .offer{line-height:1}
  .offer__label{font-size:76px}
  .offer__price{font-size:168px;line-height:.95}
  .offer__price small{font-size:90px}
  .offer__unit{font-size:96px}
  .offer--bulk{color:var(--green-bright)}
  .offer--juice{color:var(--orange-soft)}
  .offer--table{color:var(--green-text)}
  .offer--premium{color:var(--orange-red)}
</style>
</head>
<body>
<main class="banner">
  <div class="banner__ornament" role="img" aria-label="Decorazioni tradizionali siciliane verdi con motivi floreali e triscele"></div>
  <section class="banner__panel">
    <header class="brand">
      <div class="brand__mark"></div>
      <div class="brand__name">Agrumeto Solare</div>
    </header>
    <h1 class="headline">
      <div class="headline__top">Dal cuore</div>
      <div class="headline__bottom">della Sicilia</div>
    </h1>
    <div class="variety">Arancia Tarocco</div>
    <div class="offers">
      <div class="offer offer--bulk">
        <div class="offer__label">Alla rinfusa</div>
        <div class="offer__price">5<small>€</small></div>
        <div class="offer__unit">Borsa</div>
      </div>
      <div class="offer offer--juice">
        <div class="offer__label">Da spremere</div>
        <div class="offer__price">10<small>€</small></div>
        <div class="offer__unit">Cassetta</div>
      </div>
      <div class="offer offer--table">
        <div class="offer__label">Da tavola</div>
        <div class="offer__price">15<small>€</small></div>
        <div class="offer__unit">Cassetta</div>
      </div>
      <div class="offer offer--premium">
        <div class="offer__label">Selezione premium</div>
        <div class="offer__price">20<small>€</small></div>
        <div class="offer__unit">Cassetta</div>
      </div>
    </div>
  </section>
</main>
</body>
</html>
```